7 Loop Flyer

We are a gym named Korvalle and we need a flyer design for our challenge we will be having called the '7 LOOP'. The '7 LOOP' is a 6 Week Transformation Challenge where participants will train throughout the 6 weeks then see what progress they have made at the end, with prizes on offer for the best results.

We would like to see designs that use the colour blue.

The design we would like has been sketched and added in files section, subject to minor word changes later on. Both logos have also been added to the file section as well. As per the sketch, At the top should be the 'Korvalle 7 LOOP' logo. Underneath will have writing that says 'A 6 week transformation challenge that will get you in the best shape of your life!

Below that will say 'NO EGOS REAL PEOPLE REAL RESULTS' underneath each other. With 'ENTRIES NOW OPEN' below.

Then at the bottom the other Korvalle logo.

Colors
33a6d7
85cae6
0292cd
0355a3
3276b5
85abd2
e667a6
e34197

Requirements
Must have
• Mention of the prizes
• "Chance to win over $1200 in prizes"
• 1st Place $600 CASH MONEY!!!!
• Sign up now kicks off September 22
• The ultimate 6 Week Transformation
Should not have
• Generic / Stock images

```html
<!DOCTYPE html>
<html lang="en">
<head>
<meta charset="utf-8">
<title>Korvalle 7 LOOP – Flyer</title>
<link rel="stylesheet" href="https://fonts.googleapis.com/css2?family=Alfa+Slab+One&family=Bebas+Neue&family=Poppins:wght@300;600;700&family=Roboto:wght@400&family=Saira:wght@600;700&display=swap">
<style>
  :root{
    --navy:#13296b;
    --blue:#0355a3;
    --cyan:#1ea7e1;
    --sky:#85cae6;
    --paper:#ffffff;
    --panel:#ededed;
    --ink:#1b1b1b;
    --stage:#e6e8ec;
  }
  html,body{margin:0;padding:0;width:1200px;height:1200px;overflow:hidden;background:var(--stage);}
  .canvas{position:relative;width:1200px;height:1200px;}
  .flyer{
    position:absolute;left:183px;top:10px;width:868px;height:1228px;
    transform:scale(0.96);transform-origin:top left;
    background:var(--paper);overflow:hidden;
  }
  .flyer > *{position:absolute;}
  .hero-photo{
    left:0;top:0;width:868px;height:560px;
    background:linear-gradient(180deg,#c9d3e3 0%,#a9b8cf 35%,#dfe5ee 65%,#ffffff 100%);
  }
  .event-badge{
    left:528px;top:34px;width:270px;height:270px;border-radius:50%;
    background:var(--paper);display:flex;align-items:center;justify-content:center;
    flex-direction:column;text-align:center;
    font-family:"Saira",sans-serif;font-weight:700;color:var(--navy);font-size:40px;line-height:1.05;
  }
  .headline-block{left:79px;top:330px;width:703px;height:466px;background:var(--navy);}
  .intro-box{
    left:91px;top:354px;width:681px;height:192px;background:var(--paper);text-align:center;
  }
  .intro-text{
    margin:26px 0 0;font-family:"Poppins",sans-serif;font-weight:300;font-size:29px;line-height:37px;color:#2a2a2a;
  }
  .intro-title{
    margin:10px 0 0;font-family:"Saira",sans-serif;font-weight:600;font-size:47px;line-height:60px;
    color:var(--navy);letter-spacing:0.5px;white-space:nowrap;
  }
  .values-band{
    left:59px;top:567px;width:743px;height:85px;background:var(--cyan);
    display:flex;align-items:center;justify-content:center;overflow:hidden;
  }
  .values-text{
    display:inline-block;white-space:nowrap;
    font-family:"Bebas Neue",sans-serif;font-size:66px;line-height:85px;color:var(--paper);
    letter-spacing:-0.5px;word-spacing:-6px;
    transform:scaleX(0.86);transform-origin:center;
  }
  .entries-ribbon{left:167px;top:679px;width:529px;height:88px;}
  .entries-text{
    left:167px;top:679px;width:529px;height:88px;text-align:center;
    font-family:"Saira",sans-serif;font-weight:700;font-size:48px;line-height:88px;color:var(--navy);
    white-space:nowrap;
  }
  .prize-headline{
    left:0;top:824px;width:868px;text-align:center;white-space:nowrap;
    font-family:"Alfa Slab One",serif;font-size:32px;line-height:44px;color:var(--navy);letter-spacing:0.3px;
  }
  .prize-headline .amount{color:var(--blue);}
  .rule{left:104px;width:653px;height:2px;background:var(--navy);}
  .rule-top{top:890px;}
  .rule-bottom{top:963px;}
  .first-prize{
    left:0;top:898px;width:868px;text-align:center;white-space:nowrap;
    font-family:"Poppins",sans-serif;font-weight:300;font-size:40px;line-height:62px;color:var(--ink);
  }
  .first-prize .cash{font-family:"Bebas Neue",sans-serif;font-size:52px;color:var(--blue);}
  .signup-panel{left:76px;top:983px;width:710px;height:158px;background:var(--panel);}
  .signup-call{
    left:100px;top:1005px;font-family:"Poppins",sans-serif;font-weight:600;font-size:34px;line-height:46px;color:var(--cyan);margin:0;
  }
  .signup-date{
    left:100px;top:1046px;font-family:"Poppins",sans-serif;font-weight:700;font-size:28px;line-height:38px;color:var(--ink);margin:0;
  }
  .signup-note{
    left:100px;top:1084px;font-family:"Roboto",sans-serif;font-weight:400;font-size:23px;line-height:32px;color:var(--ink);margin:0;
  }
  .brand-name{
    left:532px;top:1030px;width:230px;text-align:center;
    font-family:"Saira",sans-serif;font-weight:700;font-size:50px;line-height:64px;color:var(--navy);
  }
  .site-footer{
    left:0;top:1166px;width:868px;height:62px;background:var(--navy);text-align:center;
    font-family:"Poppins",sans-serif;font-weight:300;font-size:21px;line-height:62px;color:var(--cyan);letter-spacing:5px;
  }
</style>
</head>
<body>
<div class="canvas">
  <article class="flyer">
    <div class="hero-photo" role="img" aria-label="Photo of a trainer coaching an athlete on an air bike in a bright gym"></div>

    <div class="event-badge"><span>Korvalle</span><span>7 LOOP</span></div>

    <div class="headline-block"></div>
    <div class="intro-box">
      <p class="intro-text">A 6 week transformation challenge<br>that will get you in the</p>
      <p class="intro-title">BEST SHAPE OF YOUR LIFE!</p>
    </div>

    <div class="values-band"><span class="values-text">NO EGOS | REAL PEOPLE | REAL RESULTS</span></div>

    <svg class="entries-ribbon" width="529" height="88" viewBox="0 0 529 88" aria-hidden="true">
      <polygon points="0,0 529,0 510,44 529,88 0,88 19,44" fill="#ffffff"/>
    </svg>
    <div class="entries-text">ENTRIES NOW OPEN</div>

    <div class="prize-headline">CHANCE TO WIN OVER <span class="amount">$1200</span> IN PRIZES</div>
    <div class="rule rule-top"></div>
    <div class="first-prize">1st Place <span class="cash">$600</span> CASH MONEY!!!!</div>
    <div class="rule rule-bottom"></div>

    <div class="signup-panel"></div>
    <p class="signup-call">Sign up now</p>
    <p class="signup-date">kicks off September 22</p>
    <p class="signup-note">The ultimate 6 Week Transformation</p>
    <div class="brand-name">Korvalle</div>

    <footer class="site-footer">www.korvalle.net.au</footer>
  </article>
</div>
</body>
</html>
```